Hypnotherapy- past life regression-life between lives therapist needs a website

I need a website that is enticing and spiritual in its feeling. It needs to have a lot of beautiful nature pictures included. The theme is "Quiet Harbor Path- what might you find....Lessons Solutions Answers"
Because all of us have the answers to living our best life, they are in our subconcious. But not everyone is capable of accessing them. Hypnosis accesses the subconcious and helps to create new neural pathways in the brain which can create new behaviors and responses to situations.
Hypnosis can help with anxiety, pain relief, weight loss, smoking/vaping cessation, self confidence......anything about yourself that you want to change.
Exploration of past lives and life between lives can reveal things related to ones current life. For example, perhaps your fear of deep water is a result of drowning in a past life. Once this has been discovered, it can lead to changes in ones current life.
Almost any personal behavior one wants to change, can be helped through hypnotherapy.
I need a page for testimonials, a place for scheduling (I will have a link to my scheduling app) some information about hypnotherapy.
I am uploading my logo files. My business card will be using the black and gold style, but my website does not have to reflect that. It can be based on the caramel and deep green like full color logo. Earthy, calm colors.
I also like the mock up of my logo on the beach and there was one on a starry night sky that I also liked.
Target Market(s)
men and women ages 25-50
Industry/Entity Type
natural health and wellness, spirituality
Number of Pages Required
4 page
Requirements
Must have
- a page for testimonials, perhaps with a beautiful nature picture with each one, I will have approximately 6. A link to schedule a complimentary intro session, preferably on the first page
Should not have
- no swinging watches or other sterotyped hypnosis symbols

```html
<!DOCTYPE html>
<html lang="en">
<head>
<meta charset="utf-8">
<title>Quiet Harbor Path – Hypnotherapy</title>
<link href="https://fonts.googleapis.com/css2?family=Libre+Baskerville:wght@700&family=Open+Sans:wght@400;600;700&display=swap" rel="stylesheet">
<style>
:root{
  --olive:#66652f;
  --olive-dark:#55542a;
  --orange:#e1892b;
  --ink:#4a4321;
  --text:#6c6c6c;
  --grey:#f4f4f6;
  --white:#fff;
}
*{box-sizing:border-box;margin:0;padding:0}
html,body{width:1200px;height:4841px;overflow:hidden}
body{position:relative;font-family:"Open Sans",sans-serif;color:var(--text);background:var(--white)}
.abs{position:absolute}
.serif{font-family:"Libre Baskerville",serif;color:var(--ink);font-weight:700}
.eyebrow{font-size:11px;color:var(--orange);font-weight:600;letter-spacing:.5px;display:flex;align-items:center;gap:10px}
.eyebrow::after{content:"";width:50px;height:2px;background:var(--orange)}
p.body{font-size:12.5px;line-height:24px}
.btn{display:flex;align-items:center;justify-content:center;background:var(--orange);color:#fff;font-size:13px;font-weight:700;border-radius:4px}
.photo{border-radius:0}

/* header */
.topbar{left:0;top:0;width:1200px;height:34px;background:#f1f1f1}
.topbar span{position:absolute;top:9px;font-size:13px;color:#333}
.nav{left:0;top:34px;width:1200px;height:52px;background:#fff}
.nav a{position:absolute;top:19px;font-size:12.5px;color:#555;text-decoration:none}
.nav a.active{color:var(--ink);font-weight:700}
.logo-badge{left:138px;top:0;width:166px;height:96px;border-radius:50%;background:#fff;box-shadow:0 4px 10px rgba(0,0,0,.12);display:flex;align-items:center;justify-content:center;gap:6px}
.brand{font-family:"Open Sans",sans-serif;font-weight:700;color:var(--orange);font-size:11px}
.call{left:860px;top:0;width:198px;height:86px;background:var(--olive);color:#fff;padding:22px 0 0 44px}
.call small{font-size:13px;display:block}
.call b{font-size:19px}
.call-ring{left:856px;top:26px;width:36px;height:36px;border-radius:50%;background:#fff;border:2px solid var(--orange);display:flex;align-items:center;justify-content:center}

/* hero */
.hero-photo{left:0;top:86px;width:1200px;height:780px;background:linear-gradient(170deg,#4d4230 0%,#8a6f48 40%,#a8844f 70%,#6e5534 100%)}
.hero-card{left:75px;top:270px;width:475px;height:363px;background:#fff;padding:52px 0 0 47px}
.hero-card::before{content:"";position:absolute;left:0;top:60px;width:7px;height:96px;background:var(--orange)}
.hero-card h1{font-size:55px;line-height:68px}
.hero-card p{font-size:11px;line-height:20px;margin:20px 28px 0 0}

/* about */
.about-text{left:625px;top:990px;width:470px}
.about-text h2{font-size:40px;line-height:62px;margin:22px 0 22px}

/* features */
.features{left:88px;top:1534px;width:1016px;height:213px;background:#fff;border-radius:0 0 70px 70px;box-shadow:0 8px 22px rgba(0,0,0,.08)}
.feat{position:absolute;top:36px;width:300px}
.feat .ic{position:absolute;left:0;top:0;width:64px;height:64px;border-radius:50%;border:2px solid var(--olive);display:flex;align-items:center;justify-content:center}
.feat h3{margin-left:82px;font-size:20px}
.feat em{display:block;margin:6px 0 0 82px;font-style:normal;color:#4a74b8;font-size:15px}
.feat p{margin:14px 0 0 82px;font-size:12px;line-height:24px}

/* services */
.services-bg{left:0;top:1800px;width:1200px;height:726px;background:var(--grey)}
.arrow{width:44px;height:60px;background:#fff;box-shadow:0 2px 8px rgba(0,0,0,.1);display:flex;align-items:center;justify-content:center}
.svc-card{width:282px;height:198px;background:#fff;padding:22px 0 0 30px;box-shadow:0 4px 12px rgba(0,0,0,.06)}
.svc-card h3{font-size:18px}
.svc-card p{font-size:12px;line-height:24px;margin-top:14px;color:#555}
.svc-card a{display:block;margin-top:12px;font-size:14px;font-weight:700;color:var(--orange);text-decoration:none}
.svc-card.on{background:var(--olive)}
.svc-card.on h3,.svc-card.on p,.svc-card.on a{color:#fff}

/* why */
.why-item{width:240px}
.why-item h4{font-size:14px;color:var(--ink);font-weight:700;margin-left:66px}
.why-item p{font-size:12px;line-height:24px;margin:6px 0 0 66px}
.why-item svg{position:absolute;left:10px;top:0}

/* testimonials */
.testi-bg{left:0;top:3165px;width:1200px;height:734px;background:var(--grey)}
.t-card{width:323px;height:263px;background:#fff;text-align:center;padding-top:65px}
.stars{color:var(--orange);font-size:18px;letter-spacing:8px}
.t-card p{font-size:12.5px;line-height:24px;margin:18px 44px 0}
.avatar{width:56px;height:56px;border-radius:50%;background:linear-gradient(#c7d2de,#6d87a7)}
.quote{width:70px;height:36px;border-radius:35px 35px 0 0;background:var(--olive);display:flex;align-items:center;justify-content:center;color:#fff;font-family:"Libre Baskerville",serif;font-size:26px}
.t-name{width:323px;text-align:center}
.t-name b{display:block;font-size:16px;color:#444}
.t-name span{font-size:12px}

/* contact */
.contact-photo{left:0;top:3899px;width:1200px;height:500px;background:linear-gradient(90deg,#b7aea2,#d6d2cb 50%,#e8e7e4)}
.person{left:150px;top:3747px;width:460px;height:652px;background:linear-gradient(#4a3226 0%,#e9e4dc 35%,#d8cfc2 70%,#a57b4c 100%);border-radius:200px 200px 0 0}
.form{left:652px;top:3978px;width:460px;height:477px;background:var(--olive);border:4px solid #fff;border-radius:16px;box-shadow:0 0 0 2px var(--olive);padding:34px 28px 0;text-align:center;color:#fff}
.form h2{font-size:27px;font-weight:700}
.form p{font-size:12px;line-height:18px;margin:10px 20px 30px}
.field{height:44px;background:rgba(255,255,255,.18);border-radius:5px;margin-bottom:30px;text-align:left;padding:14px 0 0 20px;font-size:9px;letter-spacing:.5px}
.submit{height:44px;background:#fff;border-radius:5px;color:var(--orange);font-size:14px;font-weight:600;padding-top:12px}

/* footer */
.foot-col h5{font-size:14px;color:#555;font-weight:600;padding-bottom:10px;border-bottom:1px solid #c9c9c9;width:120px}
.foot-col li{list-style:none;font-size:13px;line-height:32px;color:#666}
.social{width:26px;height:26px;border-radius:50%;background:#e8e8e8;display:inline-block;margin-left:8px;vertical-align:middle}
</style>
</head>
<body>

<!-- header -->
<div class="abs topbar">
  <span style="left:394px">WELCOME</span>
  <svg class="abs" style="left:626px;top:5px" width="24" height="24" viewBox="0 0 24 24"><circle cx="12" cy="12" r="11" fill="#555"/><rect x="6" y="8" width="12" height="8" fill="none" stroke="#fff" stroke-width="1.5"/><path d="M6 8l6 5 6-5" fill="none" stroke="#fff" stroke-width="1.5"/></svg>
  <span style="left:660px">hello@quietharborpath.com</span>
</div>
<nav class="abs nav">
  <a class="active" style="left:337px">HOME</a>
  <a style="left:424px">About Us</a>
  <a style="left:518px">Services</a>
  <a style="left:612px">Team</a>
  <a style="left:702px">Blog</a>
  <a style="left:773px">Contact Us</a>
</nav>
<div class="abs logo-badge"><span style="width:14px;height:14px;border-radius:50%;background:var(--orange)"></span><span class="brand">QUIET HARBOR PATH</span></div>
<div class="abs call"><small>Call us today at</small><b>(555) 010-2468</b></div>
<div class="abs call-ring"><svg width="18" height="18" viewBox="0 0 24 24"><path d="M6 3l4 4-2 3c1 2 4 5 6 6l3-2 4 4-3 3C10 21 3 14 3 6z" fill="var(--orange)"/></svg></div>

<!-- hero -->
<div class="abs hero-photo" role="img" aria-label="Woman sitting calmly in a golden grass field at sunset"></div>
<svg class="abs" style="left:0;top:740px" width="1200" height="130" viewBox="0 0 1200 130">
  <path d="M0 55 C180 110 330 110 520 80 C760 40 980 20 1200 60 L1200 130 L0 130Z" fill="#fff"/>
  <path d="M0 40 C60 90 170 110 320 88 C520 58 700 10 900 20" fill="none" stroke="var(--olive)" stroke-width="14"/>
  <path d="M200 110 C500 60 800 10 1200 70" fill="none" stroke="var(--orange)" stroke-width="6"/>
</svg>
<div class="abs hero-card">
  <h1 class="serif">Pioneers in Hypnotherapy</h1>
  <p>Lorem ipsum dolor sit amet, consectetur adipiscing elit, sed do eiusmod tempor incididunt ut labore et dolore magna aliqua. Ut enim</p>
  <div class="btn" style="width:168px;height:46px;margin-top:34px">Contact Us</div>
</div>

<!-- about -->
<div class="abs" role="img" aria-label="Therapist in session with a client" style="left:105px;top:972px;width:303px;height:315px;background:linear-gradient(135deg,#6e7a52,#c9c2b3 60%,#7d8b96);border-radius:110px 0 0 0"></div>
<div class="abs" role="img" aria-label="Client relaxing during hypnosis" style="left:430px;top:993px;width:122px;height:122px;background:linear-gradient(135deg,#c9d3dc,#8e9aa5);border-radius:0 40px 0 40px"></div>
<div class="abs" role="img" aria-label="Woman sitting outdoors in autumn woods" style="left:268px;top:1132px;width:303px;height:314px;background:linear-gradient(135deg,#6c5a33,#b07a3e 50%,#d3b08a);border-radius:0 0 150px 0"></div>
<div class="abs" style="left:238px;top:1215px;width:96px;height:96px;border-radius:50%;background:#fff;display:flex;align-items:center;justify-content:center"><span style="width:40px;height:40px;border-radius:50%;border:3px solid var(--orange)"></span></div>
<div class="abs about-text">
  <div class="eyebrow">ABOUT US</div>
  <h2 class="serif">Discover Your True Self with Hypno Insight</h2>
  <p class="body">Lorem ipsum dolor sit amet, consectetur adipiscing elit, sed do eiusmod tempor incididunt ut labore et dolore magna aliqua. Ut enim ad min im veniam, quis nostrud exercitation ullamco laboris nisi ut aliquip ex ea commodo consequat. Duis aute irure dolor in reprehenderit in voluptate velit esse cillum dolore eu fugiat nulla pariatur. Excepteur sint occaecat cupidatat non proident, sunt in culpa qui officia deserunt mollit anim id est laborum.</p>
  <div class="btn" style="width:168px;height:46px;margin-top:22px">Contact Us</div>
</div>

<!-- features -->
<div class="abs features">
  <div class="feat" style="left:60px"><div class="ic"><svg width="30" height="30" viewBox="0 0 30 30"><circle cx="15" cy="15" r="9" fill="none" stroke="var(--orange)" stroke-width="2" stroke-dasharray="3 3"/></svg></div><h3 class="serif">Experts</h3><em>Lorem Ipsum</em><p>Lorem ipsum dolor sit amet, consectetur adipiscing elit, se do eiusmod tempor e</p></div>
  <div class="feat" style="left:368px"><div class="ic"><svg width="30" height="30" viewBox="0 0 30 30"><path d="M15 5v20M5 15h20" stroke="var(--orange)" stroke-width="2" stroke-dasharray="4 3"/></svg></div><h3 class="serif">Personalized</h3><em>Lorem Ipsum</em><p>Lorem ipsum dolor sit amet, consectetur adipiscing elit, se do eiusmod tempor e</p></div>
  <div class="feat" style="left:678px"><div class="ic"><svg width="30" height="30" viewBox="0 0 30 30"><path d="M8 20a8 8 0 1 1 14 0v4H8z" fill="none" stroke="var(--orange)" stroke-width="2"/></svg></div><h3 class="serif">Innovative</h3><em>Lorem Ipsum</em><p>Lorem ipsum dolor sit amet, consectetur adipiscing elit, se do eiusmod tempor e</p></div>
</div>

<!-- services -->
<div class="abs services-bg"></div>
<div class="abs eyebrow" style="left:97px;top:1852px">ABOUT US</div>
<h2 class="abs serif" style="left:95px;top:1892px;font-size:38px">Services We Provide</h2>
<div class="abs arrow" style="left:1008px;top:1870px"><svg width="12" height="14" viewBox="0 0 12 14"><path d="M9 1L3 7l6 6" fill="none" stroke="#222" stroke-width="2.5"/></svg></div>
<div class="abs arrow" style="left:1058px;top:1870px"><svg width="12" height="14" viewBox="0 0 12 14"><path d="M3 1l6 6-6 6" fill="none" stroke="#222" stroke-width="2.5"/></svg></div>

<div class="abs" role="img" aria-label="Two people smiling in a bookshelf-lined office" style="left:90px;top:1974px;width:323px;height:234px;background:linear-gradient(135deg,#6a5a47,#b9a68e 55%,#e0d6c8)"></div>
<div class="abs" role="img" aria-label="Hands held together in support" style="left:436px;top:1974px;width:323px;height:234px;background:linear-gradient(135deg,#4d5342,#8a7f6e 50%,#c5b7a2)"></div>
<div class="abs" role="img" aria-label="Therapist talking with a client in a study" style="left:786px;top:1974px;width:323px;height:234px;background:linear-gradient(135deg,#7a6852,#b8aa97 50%,#5f6d4d)"></div>
<div class="abs svc-card" style="left:113px;top:2152px"><h3 class="serif">Emotional Healing</h3><p>Lorem ipsum dolor sit amet, consectetur adipiscing elit, sed do eiusmod tempor incididunt ut nn</p><a>Read More</a></div>
<div class="abs svc-card on" style="left:456px;top:2152px"><h3 class="serif">Past Life Regression</h3><p>Lorem ipsum dolor sit amet, consectetur adipiscing elit, sed do eiusmod tempor incididunt ut nn</p><a>Read More</a></div>
<div class="abs svc-card" style="left:806px;top:2152px"><h3 class="serif">Phobia Resolution</h3><p>Lorem ipsum dolor sit amet, consectetur adipiscing elit, sed do eiusmod tempor incididunt ut nn</p><a>Read More</a></div>
<div class="abs btn" style="left:513px;top:2391px;width:167px;height:47px;background:#fff;border:1px solid var(--orange);color:var(--orange);font-weight:600">Contact Us</div>

<!-- why choose -->
<div class="abs eyebrow" style="left:93px;top:2612px">WHY CHOOSE US</div>
<h2 class="abs serif" style="left:91px;top:2645px;font-size:38px;line-height:60px">Mind Mastery,<br>Life Transformation</h2>
<p class="abs body" style="left:93px;top:2775px;width:440px;font-size:12px">Lorem ipsum dolor sit amet, consectetur adipiscing elit, sed do eiusmod tempor incididunt ut labore et dolore magna aliqua. Ut enim ad min im veniam, quis nostrud exercitation ij</p>
<div class="abs why-item" style="left:93px;top:2880px"><svg width="30" height="30" viewBox="0 0 30 30"><path d="M4 6h8v6H4zM18 18h8v6h-8zM12 9h6v12M4 21h8" fill="none" stroke="var(--orange)" stroke-width="2"/></svg><h4>Proven Results</h4><p>Lorem ipsum dolor sit amet, consectetur adipiscing elit.</p></div>
<div class="abs why-item" style="left:357px;top:2880px"><svg width="30" height="30" viewBox="0 0 30 30"><circle cx="15" cy="6" r="3" fill="var(--orange)"/><path d="M4 12h22M15 12v8l-6 8M15 20l6 8" fill="none" stroke="var(--orange)" stroke-width="2"/></svg><h4>Client-centric</h4><p>Lorem ipsum dolor sit amet, consectetur adipiscing elit.</p></div>
<div class="abs why-item" style="left:93px;top:2977px"><svg width="30" height="30" viewBox="0 0 30 30"><circle cx="8" cy="10" r="3" fill="var(--orange)"/><path d="M3 20c0-4 10-4 10 0M16 10h12M16 15h12M16 20h12" fill="none" stroke="var(--orange)" stroke-width="2"/></svg><h4>Quality Assurance</h4><p>Lorem ipsum dolor sit amet, consectetur adipiscing elit.</p></div>
<div class="abs why-item" style="left:357px;top:2977px"><svg width="30" height="30" viewBox="0 0 30 30"><circle cx="20" cy="6" r="3" fill="var(--orange)"/><path d="M4 28V18M10 28V14M16 28V20M20 10v8l4 4v6" fill="none" stroke="var(--orange)" stroke-width="2"/></svg><h4>Personalized Approach</h4><p>Lorem ipsum dolor sit amet, consectetur adipiscing elit.</p></div>
<svg class="abs" style="left:640px;top:2616px" width="470" height="470" viewBox="0 0 470 470"><path d="M30 240A205 205 0 0 1 445 230" fill="none" stroke="var(--orange)" stroke-width="7"/><path d="M445 230A205 205 0 0 1 360 400" fill="none" stroke="var(--orange)" stroke-width="4"/></svg>
<div class="abs" role="img" aria-label="Smiling woman outdoors in warm evening light" style="left:648px;top:2644px;width:455px;height:444px;border-radius:50%;background:radial-gradient(circle at 50% 40%,#c8a589,#8c8a6c 60%,#5f6b55)"></div>

<!-- testimonials -->
<div class="abs testi-bg"></div>
<div class="abs" style="left:497px;top:3227px;font-size:11px;color:var(--orange);font-weight:600">——— TESTIMONIALS ———</div>
<h2 class="abs serif" style="left:0;top:3255px;width:1190px;text-align:center;font-size:38px">What Clients are Saying</h2>

<div class="abs t-card" style="left:90px;top:3392px"><div class="stars">★★★★★</div><p>Lorem ipsum dolor sit amet, consectetur adipiscing elit, sed do eiusmod tempor incididunt ut labore et dolore</p></div>
<div class="abs t-card" style="left:441px;top:3392px"><div class="stars">★★★★★</div><p>Lorem ipsum dolor sit amet, consectetur adipiscing elit, sed do eiusmod tempor incididunt ut labore et dolore</p></div>
<div class="abs t-card" style="left:791px;top:3392px"><div class="stars">★★★★★</div><p>Lorem ipsum dolor sit amet, consectetur adipiscing elit, sed do eiusmod tempor incididunt ut labore et dolore</p></div>
<div class="abs avatar" role="img" aria-label="Client portrait" style="left:224px;top:3362px"></div>
<div class="abs avatar" role="img" aria-label="Client portrait" style="left:574px;top:3362px"></div>
<div class="abs avatar" role="img" aria-label="Client portrait" style="left:924px;top:3362px"></div>
<div class="abs quote" style="left:217px;top:3620px">“</div>
<div class="abs quote" style="left:567px;top:3620px">“</div>
<div class="abs quote" style="left:917px;top:3620px">“</div>
<div class="abs t-name" style="left:90px;top:3688px"><b>Mara Ellison</b><span>Los Angeles</span></div>
<div class="abs t-name" style="left:441px;top:3688px"><b>Mara Ellison</b><span>Los Angeles</span></div>
<div class="abs t-name" style="left:791px;top:3688px"><b>Mara Ellison</b><span>Los Angeles</span></div>

<!-- contact -->
<div class="abs contact-photo" role="img" aria-label="Bright office interior"></div>
<div class="abs person" role="img" aria-label="Woman holding a tablet and smiling"></div>
<div class="abs form">
  <h2>Connect With Us</h2>
  <p>Lorem ipsum dolor sit amet, consectetur adipiscing elit, sed do eiusmod tempor incididunt ut</p>
  <div class="field">NAME</div>
  <div class="field">EMAIL</div>
  <div class="field">MESSAGE</div>
  <div class="submit">SUBMIT NOW</div>
</div>

<!-- footer -->
<div class="abs" style="left:112px;top:4540px;display:flex;align-items:center;gap:8px"><span style="width:22px;height:22px;border-radius:50%;background:var(--orange)"></span><span class="brand" style="font-size:13px">QUIET HARBOR PATH</span></div>
<div class="abs" style="left:113px;top:4675px;font-size:13px;color:#555">Follow Us <span class="social"></span><span class="social"></span><span class="social"></span></div>
<div class="abs foot-col" style="left:364px;top:4553px"><h5>Quick Links</h5><ul style="margin-top:10px"><li>Home</li><li>About us</li><li>Services</li><li>Contact us</li></ul></div>
<div class="abs foot-col" style="left:586px;top:4553px"><h5>Contact</h5>
  <ul style="margin-top:10px">
    <li style="padding-left:48px;line-height:24px;position:relative"><svg class="abs" style="left:20px;top:4px" width="14" height="18" viewBox="0 0 14 18"><path d="M7 0a7 7 0 0 1 7 7c0 5-7 11-7 11S0 12 0 7a7 7 0 0 1 7-7z" fill="#3a5fa8"/><circle cx="7" cy="7" r="2.5" fill="#fff"/></svg>88 Meadow Lane<br>Suite 12</li>
    <li style="padding-left:48px;position:relative;margin-top:4px"><svg class="abs" style="left:18px;top:8px" width="16" height="16" viewBox="0 0 24 24"><path d="M6 3l4 4-2 3c1 2 4 5 6 6l3-2 4 4-3 3C10 21 3 14 3 6z" fill="#3a5fa8"/></svg>1-555-010-7788</li>
    <li style="padding-left:48px;position:relative"><svg class="abs" style="left:18px;top:10px" width="16" height="12" viewBox="0 0 16 12"><rect width="16" height="12" fill="#3a5fa8"/><path d="M0 0l8 6 8-6" fill="none" stroke="#fff"/></svg>hello@quietharborpath.com</li>
  </ul>
</div>
<div class="abs foot-col" style="left:860px;top:4553px"><h5>Join our Newsletter</h5>
  <p style="font-size:12.5px;line-height:18px;margin-top:16px;width:220px">Sign up for our newsletter to know the latest from us</p>
  <div style="display:flex;margin-top:8px;width:248px;height:34px;border:1px solid #ddd"><span style="flex:1;font-size:11px;padding:9px 14px;color:#999">Email</span><span style="width:98px;background:var(--orange);color:#fff;font-size:11px;font-weight:700;padding-top:10px;text-align:center">SUBSCRIBE</span></div>
</div>
<div class="abs" style="left:113px;top:4770px;width:984px;height:1px;background:#bbb"></div>
<div class="abs" style="left:0;top:4793px;width:1182px;text-align:center;font-size:12px;color:#444">QUIET HARBOR PATH</div>

</body>
</html>
```